Insurance Law Website

**Please note do not sell insurance, we are a law firm which specialises in Insurance law.**

We are a legal insurance firm based in Australia consisting of 150+ legal professionals.

Our initial budget for this project is around: $500

We require a design to meet the specification below, however we do want designers to come up with an interpretation of something modern but still professional, we need it to stand out above all other legal websites!

1. Responsive design
2. It should be a minimalist design, the use of background imagery is fine but we are looking to de-clutter the home page in particular and have additional content accessible through menu links to other areas such as publications, news, announcements and expert/staff pages, careers etc.
3. Something that stands out from a typical legal website.
4. The homepage should cater for a video which will contain a 'who we are' message from the CEO/Firm.
5. Colours used light/medium blues (eg: #8aabff, #bdd7fc), white
6. We also require a static information box on the page with the heading "THREE STATES, ONE FOCUS" - see image attached for full text of the box.

Visitors to our website should be aware we are an Insurance law firm, this can be achieved by using insurance focused full background imagery (no natural disasters such as floods, earthquakes etc) such as insurance buildings (Harwick building - London), international landmarks etc

Some websites we like certain aspects of;

http://pellambraithwaite.com/ - top image boxes
http://www.vantel.com.au/ - similar however prefer to use a FULL background image, with one full width text box at the bottom, navigation menu at the top with logo

However please don't take these examples as a sign of what the site MUST look like, please use your imagination to interpret your own vision.

Reason: Extended due to feedback provided and waiting for resubmission of designs. It appears that some people may be misunderstanding the brief, please review the brief in full before submitting any designs and let us know if you have any questions.

Reason: Apologies to those who are waiting for a decision we are reviewing and discussiing all submitted designs internally and waiting for some additional amendments to come in. We have extended the project a final time whilst we carry out our reviews. Please continue to submit any modifications and thanks again for everyone's input thus far. D+T

We have 3 days left of this project please keep submitting your designs. This is a guaranteed project.

D+T

Target Market(s)

Lawyers looking for publications, information, contact details of our lawyers and careers/job searches.

Industry/Entity Type

Insurance

Font styles to use
Sans Serif

Requirements
Must have
• Top menu to include:

Home (small icon)
Who We Are (text)
Experts (text)
Expertise (text)
Media (text)
- News (text)
- Publications (text)
Community Footprint (text)
Careers (text)
Contact (text/icon)
Search (icon - will expand on click to search in field)

Footer to include:

Copyright (text)
Privacy Policy (text)
Cookie policy (text)
Sitemap (text)
Contact (text/icon)
Chainbook (icon)
Print (icon)
Email (icon)

Should not have
• Stereotypical imagery such as legal scales, money bags, natural disasters etc. We are a professional firm and require designs to suit.

```html
<!DOCTYPE html>
<html lang="en">
<head>
<meta charset="utf-8">
<title>Marlow Kendrick – Home</title>
<link href="https://fonts.googleapis.com/css2?family=Lato:wght@300;400;700&display=swap" rel="stylesheet">
<style>
  :root {
    --blue: #8aabff;
    --blue-dark: #7696ea;
    --blue-pale: #bdd7fc;
    --logo-blue: #1f4fa8;
    --white: #ffffff;
    --footer-bg: #fbfbfb;
    --ink: #222a36;
    --player-bar: #2a2d31;
    --progress: #1aa3e8;
  }
  * { margin: 0; padding: 0; box-sizing: border-box; }
  html, body { width: 1200px; height: 653px; overflow: hidden; }
  body { font-family: "Lato", sans-serif; background: var(--white); position: relative; }

  .site-header { position: absolute; left: 0; top: 0; width: 1200px; height: 84px; background: var(--white); }
  .brand { position: absolute; left: 200px; top: 14px; display: flex; align-items: center; gap: 10px; }
  .brand-name { font-size: 26px; line-height: 24px; font-weight: 400; color: var(--logo-blue); letter-spacing: -0.3px; width: 118px; }
  .brand-mark { width: 8px; height: 8px; background: var(--blue-pale); }

  .search-icon { position: absolute; left: 982px; top: 17px; }

  .main-nav { position: absolute; right: 200px; top: 52px; display: flex; align-items: center; }
  .main-nav a { font-size: 14px; letter-spacing: -0.4px; color: var(--blue); text-decoration: none; padding: 0 4px; position: relative; height: 31px; line-height: 24px; }
  .main-nav a.active { color: var(--blue-dark); }
  .main-nav a.active::after { content: ""; position: absolute; left: 0; right: 0; bottom: 0; height: 3px; background: var(--blue); }
  .main-nav .sep { width: 1px; height: 10px; background: #d2d8e4; margin: 0 4px 6px; }
  .caret { display: inline-block; width: 0; height: 0; border-left: 4px solid transparent; border-right: 4px solid transparent; border-top: 5px solid var(--blue); margin-left: 3px; vertical-align: middle; }

  .hero { position: absolute; left: 0; top: 84px; width: 1200px; height: 506px;
    background:
      radial-gradient(ellipse at 45% 25%, #d9dde0 0%, rgba(200,205,208,0.6) 30%, rgba(0,0,0,0) 60%),
      linear-gradient(90deg, #2e3a3e 0%, #586a70 22%, #8d9a9d 45%, #9aa3a3 62%, #6f7b7c 80%, #8a9494 100%); }

  .video-frame { position: absolute; left: 220px; top: 203px; width: 326px; height: 210px; border: 1px solid rgba(255,255,255,0.75);
    background: linear-gradient(160deg, rgba(40,55,65,0.55), rgba(150,165,170,0.35) 60%, rgba(220,225,228,0.4)); }
  .play-button { position: absolute; left: 140px; top: 78px; }
  .player-bar { position: absolute; left: 0; bottom: 0; width: 100%; height: 19px; background: var(--player-bar); display: flex; align-items: center; padding: 0 6px; gap: 6px; }
  .progress { position: relative; width: 212px; height: 6px; background: #55595e; }
  .progress span { position: absolute; left: 0; top: 0; height: 100%; width: 89%; background: var(--progress); }
  .timecode { position: absolute; left: 180px; top: -12px; font-size: 7px; background: #eee; color: #555; padding: 0 3px; }
  .volume { width: 19px; height: 7px; background: repeating-linear-gradient(90deg, var(--progress) 0 1px, transparent 1px 3px); }
  .hd { font-size: 8px; font-weight: 700; color: #555; }
  .player-name { font-size: 10px; font-weight: 700; color: var(--white); }

  .info-box { position: absolute; left: 578px; top: 252px; width: 400px; color: var(--white); }
  .info-title { font-size: 40px; font-weight: 400; letter-spacing: -2px; line-height: 44px; }
  .info-title strong { font-weight: 700; color: var(--blue); font-size: 36px; letter-spacing: -2px; }
  .info-text { font-size: 14.5px; font-weight: 400; letter-spacing: -0.6px; line-height: 17.5px; margin-top: 1px; }

  .site-footer { position: absolute; left: 0; top: 590px; width: 1200px; height: 62px; background: var(--footer-bg); border-bottom: 1px solid #e2e2e2; }
  .footer-line { position: absolute; right: 200px; top: 22px; display: flex; align-items: center; font-size: 10px; color: var(--ink); }
  .footer-line b { font-weight: 700; margin-left: 3px; }
  .footer-line a { color: #2b3d6a; text-decoration: none; font-size: 10.5px; }
  .footer-line .bar { margin: 0 3px; }
  .social { display: flex; gap: 3px; margin-left: 8px; }
  .social span { width: 19px; height: 19px; border-radius: 50%; display: block; }
  .social .chainbook { background: #1a6fa8; }
  .social .print { background: #d9262f; }
  .social .email { background: #f7b547; }
</style>
</head>
<body>
  <header class="site-header">
    <div class="brand">
      <span class="brand-name">marlow kendrick</span>
      <span class="brand-mark"></span>
    </div>
    <svg class="search-icon" width="20" height="20" viewBox="0 0 20 20" aria-label="Search">
      <circle cx="12.5" cy="7.5" r="5" fill="none" stroke="#a9c0ff" stroke-width="2.4"/>
      <line x1="9" y1="11" x2="2.5" y2="17.5" stroke="#a9c0ff" stroke-width="3" stroke-linecap="round"/>
    </svg>
    <nav class="main-nav">
      <a class="active" href="#">Home</a><span class="sep"></span>
      <a href="#">Who We Are</a><span class="sep"></span>
      <a href="#">Experts</a><span class="sep"></span>
      <a href="#">Expertise</a><span class="sep"></span>
      <a href="#">Media<span class="caret"></span></a><span class="sep"></span>
      <a href="#">Careers</a><span class="sep"></span>
      <a href="#">Community Footprint</a><span class="sep"></span>
      <a href="#">Contact</a>
    </nav>
  </header>

  <main class="hero" role="img" aria-label="Upward view of a glass and steel office tower against a cloudy sky">
    <div class="video-frame">
      <svg class="play-button" width="44" height="44" viewBox="0 0 44 44" aria-label="Play video">
        <circle cx="22" cy="22" r="20" fill="none" stroke="#fff" stroke-width="3"/>
        <path d="M18 14 L31 22 L18 30 Z" fill="#fff"/>
      </svg>
      <div class="player-bar">
        <div class="progress"><span></span><em class="timecode">02:04</em></div>
        <div class="volume"></div>
        <span class="hd">HD</span>
        <svg width="8" height="8" viewBox="0 0 8 8"><path d="M0 0h3M0 0v3M8 0h-3M8 0v3M0 8h3M0 8v-3M8 8h-3M8 8v-3" stroke="#fff" stroke-width="1.4"/></svg>
        <span class="player-name">reelbox</span>
      </div>
    </div>

    <section class="info-box">
      <h1 class="info-title">Three States<strong>ONE FOCUS</strong></h1>
      <p class="info-text">Our insurance specialists have many years of experience and expertise in providing the best coverage at the lowest possible price for country clubs throughout the east coast.specialists have many years of experience and expertise.</p>
    </section>
  </main>

  <footer class="site-footer">
    <div class="footer-line">
      COPYRIGHT © 2013 <b>MARLOW KENDRICK</b>
      <span class="bar">|</span><a href="#">Cookie Policy</a>
      <span class="bar">|</span><a href="#">Sitemap</a>
      <span class="bar">|</span>
      <div class="social">
        <span class="chainbook" aria-label="Chainbook"></span>
        <span class="print" aria-label="Print"></span>
        <span class="email" aria-label="Email"></span>
      </div>
    </div>
  </footer>
</body>
</html>
```